Honey jar label for small US farm

My daughters have 6 beehives and will be producing 300-400 jars of honey this season that they plan to sell at the farmers' market.
We are looking for a label design for small honey jars.
Label size:  1.5 inches high and 3 inches wide.
The label will be a simple RECTANGLE (no special cut)
We would like a playful look but upscale enough. We don't think that flowers or bees add anything. We like cleaner looks but not cold.
Maybe one could also represent the 3 sisters somewhere on the label. As elegant stick figures maybe?
One could also imagine a design where the label is black and the text/images are white to add some dramatic effect. The jar lid is black.
The honey is raw, un-pasturized, straight from the beehive.

Target Market(s)
Farm stand, sold by the 3 sisters who are 11, 9 and 6
Industry/Entity Type
Food Production
Colors
Designer to choose colors to be used in the design.
Requirements
Must have
- Name (means three sisters in English): Val Doux
- What it is: Berkshire Raw Honey
- Net weight: 3.75oz (110ml)
- Location: Maple Hollow, MA
- Text on one of the sides: Sister to sister we will always be, a couple of nuts off the family tree!
- Note that the jar is an hexagon. See the attached STOCK photo.
- Therefore, a little more than 1 inch is on the front facing, and 0.75 inches on each sides.

Nice to have
- The design should be elegant (but not ornate), but clean. Inviting and fun.
- No need for bees or flowers which would not make it look upscale.
- No gold or "over the top" fancy. Modern but not cold.
- Remember that this is a honey brand for 3 young sisters. Something playful but upscale would work too.
- Not sure about color codes. We are quite happy staying in grey scales, but a little bit of colour might work too.

Should not have
- No UPC code needed

```html
<!DOCTYPE html>
<html lang="en">
<head>
<meta charset="utf-8">
<title>Val Doux – Berkshire Raw Honey Label</title>
<link href="https://fonts.googleapis.com/css2?family=Zilla+Slab:wght@700&family=Oswald:wght@600&family=Arimo:wght@400;700&display=swap" rel="stylesheet">
<style>
  :root {
    --stage: #050505;
    --label: #3b3b3d;
    --label-edge: #333335;
    --seam: rgba(255, 255, 255, 0.07);
    --ink: #ffffff;
    --honey: #f6c414;
    --figures: #4a4a4d;
  }
  * { box-sizing: border-box; margin: 0; padding: 0; }
  html, body {
    width: 1200px;
    height: 808px;
    overflow: hidden;
    background: var(--stage);
  }
  .stage {
    width: 1200px;
    height: 808px;
    display: flex;
    align-items: center;
    justify-content: center;
  }
  .label {
    width: 1000px;
    height: 560px;
    background: var(--label);
    display: grid;
    grid-template-columns: 250px 500px 250px;
    color: var(--ink);
    font-family: "Arimo", Arial, sans-serif;
  }
  .panel {
    position: relative;
    height: 100%;
  }
  .panel--side { background: var(--label-edge); }
  .panel--left { border-right: 1px solid var(--seam); }
  .panel--right { border-left: 1px solid var(--seam); }

  .motto {
    position: absolute;
    top: 70px;
    left: 24px;
    right: 24px;
    font-size: 22px;
    line-height: 1.4;
    text-align: center;
  }
  .side-icon {
    position: absolute;
    width: 40px;
    height: 48px;
    background: var(--honey);
    border-radius: 6px;
  }
  .side-icon--dipper { left: 44px; top: 360px; }
  .side-icon--bee { right: 44px; top: 345px; }
  .location {
    position: absolute;
    right: 24px;
    bottom: 36px;
    font-size: 18px;
    font-weight: 700;
  }

  .panel--front {
    display: flex;
    flex-direction: column;
    align-items: center;
  }
  .brand {
    margin-top: 70px;
    font-family: "Zilla Slab", Georgia, serif;
    font-weight: 700;
    font-size: 76px;
    line-height: 0.95;
    letter-spacing: 3px;
    text-align: center;
    color: var(--honey);
  }
  .product {
    margin-top: 44px;
    font-family: "Oswald", Impact, sans-serif;
    font-weight: 600;
    font-size: 34px;
    letter-spacing: 2px;
  }
  .sisters {
    margin-top: 22px;
    width: 250px;
    height: 110px;
    background: linear-gradient(180deg, var(--figures), var(--label));
    border-radius: 6px;
  }
  .ground {
    display: block;
    margin-top: -8px;
  }
  .net-weight {
    margin-top: 30px;
    font-size: 22px;
    font-weight: 700;
  }
</style>
</head>
<body>
  <main class="stage">
    <section class="label">
      <div class="panel panel--side panel--left">
        <p class="motto">Sister to sister<br>we will always be,<br>a couple of nuts<br>off the family tree!</p>
        <div class="side-icon side-icon--dipper" role="img" aria-label="Small honey dipper icon"></div>
      </div>

      <div class="panel panel--front">
        <p class="brand">VAL<br>DOUX</p>
        <h1 class="product">BERKSHIRE RAW HONEY</h1>
        <div class="sisters" role="img" aria-label="Line drawing of three sisters holding hands"></div>
        <svg class="ground" width="260" height="22" viewBox="0 0 260 22" aria-hidden="true">
          <path d="M2 20 Q130 -4 258 20 Q130 9 2 20 Z" fill="var(--honey)"/>
        </svg>
        <p class="net-weight">3.75oz (110ml)</p>
      </div>

      <div class="panel panel--side panel--right">
        <div class="side-icon side-icon--bee" role="img" aria-label="Small bee icon"></div>
        <p class="location">Maple Hollow, MA</p>
      </div>
    </section>
  </main>
</body>
</html>
```